Watch brand needs new business cards

Kestrel Timepiece Company are looking for a new business card design incorporating our logo and brand colours as per our website.

Design should be 90x55mm with 3mm print margin from edges and 3mm external bleed.

Card should be double sided, e.g. logo one side, personal details on the other.

Logo will be provided as a vector.

The card must be able to show:
- Staff name
- Position
- Office Address
- Email
- Telephone number
- Website address

Final work must be provided in an editable format to allow us to add staff details (e.g. an AI or PSD file).

```html
<!DOCTYPE html>
<html lang="en">
<head>
<meta charset="utf-8">
<title>Kestrel Timepiece Company – Business Cards</title>
<link rel="stylesheet" href="https://fonts.googleapis.com/css2?family=Barlow:wght@400;500;600;700&display=swap">
<style>
  :root {
    --ink: #0b0b0b;
    --gold: #e2ac3f;
    --paper: #ffffff;
    --stage: #ffffff;
    --faint: #6e6e6e;
    --text: #111111;
    --edge: #c4c4c4;
  }
  * { box-sizing: border-box; margin: 0; padding: 0; }
  html, body { width: 1115px; height: 1200px; overflow: hidden; }
  body {
    background: var(--stage);
    font-family: "Barlow", Arial, sans-serif;
    position: relative;
  }
  .card {
    position: absolute;
    top: 445px;
    width: 500px;
    height: 309px;
    overflow: hidden;
  }
  /* Front */
  .card-front { left: 37px; background: var(--ink); }
  .brand-mark {
    position: absolute;
    left: 192px; top: 52px;
    width: 116px; height: 116px;
    border: 6px solid var(--paper);
    border-radius: 50%;
  }
  .brand-name {
    position: absolute;
    left: 0; right: 0; top: 184px;
    text-align: center;
    color: var(--paper);
    font-weight: 600;
    font-size: 25px;
    letter-spacing: 2px;
    text-transform: uppercase;
  }
  .web-band {
    position: absolute;
    left: 0; right: 0; top: 255px;
    height: 23px;
    background: var(--gold);
    color: var(--ink);
    font-weight: 600;
    font-size: 14px;
    letter-spacing: 1.6px;
    line-height: 23px;
    padding-left: 118px;
  }
  /* Back */
  .card-back {
    left: 578px;
    background: var(--paper);
    border: 1px solid var(--edge);
  }
  .back-panel {
    position: absolute;
    left: 0; top: 0; bottom: 0;
    width: 165px;
    background: var(--ink);
    overflow: hidden;
  }
  .back-panel svg { position: absolute; left: 0; top: 0; }
  .gold-rule {
    position: absolute;
    left: 165px; top: 0; bottom: 0;
    width: 15px;
    background: var(--gold);
  }
  .staff-name {
    position: absolute;
    left: 216px; top: 60px;
    font-weight: 700;
    font-size: 19px;
    letter-spacing: 0.4px;
    color: var(--text);
  }
  .staff-position {
    position: absolute;
    left: 216px; top: 86px;
    font-weight: 500;
    font-size: 13px;
    letter-spacing: 3px;
    color: var(--text);
  }
  .contact-list { position: absolute; left: 216px; top: 150px; list-style: none; }
  .contact-item {
    display: flex;
    align-items: center;
    gap: 12px;
    height: 38px;
    margin-bottom: 8px;
  }
  .contact-icon {
    width: 26px; height: 26px;
    background: var(--ink);
    border-radius: 3px;
    display: flex; align-items: center; justify-content: center;
    flex-shrink: 0;
  }
  .contact-text {
    font-size: 14px;
    line-height: 15px;
    color: var(--text);
  }
</style>
</head>
<body>

<section class="card card-front" aria-label="Business card front">
  <div class="brand-mark"></div>
  <div class="brand-name">Kestrel Timepiece Company</div>
  <div class="web-band">www.kestreltimepiece.com.au</div>
</section>

<section class="card card-back" aria-label="Business card back">
  <div class="back-panel">
    <svg width="165" height="309" viewBox="0 0 165 309" aria-hidden="true">
      <circle cx="118" cy="162" r="122" fill="none" stroke="var(--faint)" stroke-width="14"/>
    </svg>
  </div>
  <div class="gold-rule"></div>

  <div class="staff-name">NAME SURNAME</div>
  <div class="staff-position">POSITION</div>

  <ul class="contact-list">
    <li class="contact-item">
      <span class="contact-icon">
        <svg width="16" height="16" viewBox="0 0 24 24"><path fill="var(--gold)" d="M6.6 10.8a15.1 15.1 0 0 0 6.6 6.6l2.2-2.2a1 1 0 0 1 1-.25 11.4 11.4 0 0 0 3.6.57 1 1 0 0 1 1 1V20a1 1 0 0 1-1 1A17 17 0 0 1 3 4a1 1 0 0 1 1-1h3.5a1 1 0 0 1 1 1c0 1.25.2 2.45.57 3.57a1 1 0 0 1-.25 1z"/></svg>
      </span>
      <span class="contact-text">+357 99410527<br>+357 99410527</span>
    </li>
    <li class="contact-item">
      <span class="contact-icon">
        <svg width="18" height="18" viewBox="0 0 24 24" fill="none" stroke="var(--gold)" stroke-width="1.8"><circle cx="12" cy="12" r="9"/><ellipse cx="12" cy="12" rx="4" ry="9"/><path d="M3 12h18M4.5 7.5h15M4.5 16.5h15"/></svg>
      </span>
      <span class="contact-text">email@email.com<br>www.kestreltimepiece.com.au</span>
    </li>
    <li class="contact-item">
      <span class="contact-icon">
        <svg width="16" height="16" viewBox="0 0 24 24"><path fill="var(--gold)" d="M12 2a7 7 0 0 0-7 7c0 5.25 7 13 7 13s7-7.75 7-13a7 7 0 0 0-7-7zm0 9.5A2.5 2.5 0 1 1 12 6.5a2.5 2.5 0 0 1 0 5z"/></svg>
      </span>
      <span class="contact-text">office address<br>melbourne</span>
    </li>
  </ul>
</section>

</body>
</html>
```